QUORVIX - Sydney Based Technology Consultancy -Logo & Business Card design

Who are we?
-
Quorvix is an emerging and advanced technology consulting and professional services business based in Sydney, Australia. Quorvix specialising in increasing value to organisations through the effective use of current and emerging technologies, ensuring that technology is a sustainable catalyst to attaining stated business goals.

We pride ourselves in challenging the norm.

What do we want?
-
We are looking to update our "Brand" we already have a simple “home grown” logo and we are now looking for a new one, once we have this updated logo and businesses look and feel though the business card design we will refresh our website with the new logo and design thus updating the Companies overall look at feel.

Our current site is www.quorvix-example.net.au is a very basic wordpress site and we will be updating it once we have the new logo and designs done

Our initial thoughts on the new Quorvix identity are
• Logo Concept
- One of the key things is obviously the 8
- I was thinking that a logo that had 8 as the core of the logo would be cool,
- Almost like having a “ring” or hoop that is twisted to form an 8 with different services scribed on the inside.
- So we would have a Large 8 and the inside would have ring each service or section engraved.

• Brand / web Feel
- Simple
- Professional
- Innovative
- Clear
- Destination
- Unique
- Impartial
- Safe
- Leading edge
- Familiar

- Emerging technologies
- White and ice / glacier blue
- The familiar feel of the Brindle web site
- Embedded specialist Video clips

• Portfolio of Services
- Quorvix – A smart place for Smart people
- Quorvix – we provide the process to take ideas from awareness to reality
- Focus should be on the brand quality consistent clear local knowledge with regional, national, theatre and global presence

Access to Specialists
- Emerging technologies
- Sustainability
- Collaboration
- Data centre
- Virtualisation

• Adjacent ideas under the one Brand
- Tembrosk – Enable Business Collaboration
- Plinsk – Infrastructure Virtualisation
- morvo - smart people and processes
- skandel - Emerging technologies
- brunhavel - business to technology integration
- tolpin - Smart Infrastructure
- yusk – Connected communities
- dwol - sustainability

Target Market(s)

Australia, New Zealand and Asia pacific organisations that are typically English speaking.
Markets
- IT & Technology partners
- Banking and Finance
- Health

Industry/Entity Type

Business

Requirements
Must have
• Logo
Business cards
Colour pallette
3D Logo
Nice to have
• Style guide
Designer who can also assist with new Wordpress design
Should not have
• we don't want cheap looking, overtly flashy or gimmicky logo.

```html
<!DOCTYPE html>
<html lang="en">
<head>
<meta charset="utf-8">
<title>Quorvix – Business Cards</title>
<link rel="stylesheet" href="https://fonts.googleapis.com/css2?family=Questrial&display=swap">
<style>
  :root {
    --backdrop: #e6e4e0;
    --ice-top: #cfdde2;
    --ice-bottom: #f4f7f8;
    --night-top: #3a3d42;
    --night-bottom: #121315;
    --glacier: #8fc3cf;
    --glacier-deep: #5f8f99;
    --ink-dark: #2b2e31;
    --ink-light: #f1f4f5;
    --ghost-on-dark: rgba(255,255,255,0.09);
    --ghost-on-light: rgba(120,140,148,0.22);
    --strip-top: #ffffff;
    --strip-bottom: #2c2d2f;
  }
  * { box-sizing: border-box; margin: 0; padding: 0; }
  html, body {
    width: 1200px; height: 823px; overflow: hidden;
    background: var(--backdrop);
    font-family: "Questrial", "Century Gothic", sans-serif;
  }
  .sheet { position: relative; width: 1200px; height: 823px; }
  .card {
    position: absolute; width: 510px; height: 325px;
    border-radius: 18px; overflow: hidden;
    box-shadow: 0 6px 14px rgba(0,0,0,0.25);
  }
  .card--ice { background: linear-gradient(180deg, var(--ice-top), var(--ice-bottom)); }
  .card--night { background: linear-gradient(180deg, var(--night-top), var(--night-bottom)); }
  .card--front-ice { left: 65px; top: 70px; }
  .card--back-night { left: 625px; top: 70px; }
  .card--front-night { left: 65px; top: 428px; }
  .card--back-ice { left: 625px; top: 428px; }

  .wordmark {
    position: absolute; left: 0; right: 0; top: 50%;
    transform: translateY(-50%);
    text-align: center; font-size: 78px; letter-spacing: 2px;
    color: var(--glacier-deep);
  }
  .card--night .wordmark { color: var(--glacier); }

  .services {
    position: absolute; right: 22px; top: 22px;
    text-align: right; font-size: 32px; line-height: 34px;
    color: var(--ghost-on-dark);
  }
  .card--back-ice .services { right: 42px; color: var(--ghost-on-light); }

  .ghost-name {
    position: absolute; left: 0; bottom: 18px;
    font-size: 96px; letter-spacing: 2px;
    color: var(--ghost-on-dark);
  }
  .card--back-ice .ghost-name { left: 40px; bottom: 70px; color: var(--ghost-on-light); }

  .contact { position: absolute; }
  .card--back-night .contact { left: 38px; top: 126px; color: var(--ink-light); }
  .card--back-night .contact__name { color: var(--glacier); font-size: 27px; margin-bottom: 8px; }
  .card--back-night .contact__line { font-size: 15px; line-height: 20px; }
  .card--back-ice .contact { left: 42px; top: 150px; color: var(--ink-dark); }
  .card--back-ice .contact__name { font-size: 36px; margin-bottom: 4px; }
  .card--back-ice .contact__line { font-size: 17px; line-height: 19px; padding-left: 8px; }

  .edge-strip {
    position: absolute; right: 0; top: 0; width: 28px; height: 100%;
    background: linear-gradient(180deg, var(--strip-top) 10%, var(--strip-bottom));
  }
</style>
</head>
<body>
<main class="sheet">
  <section class="card card--ice card--front-ice">
    <div class="wordmark">Quorvix</div>
  </section>

  <section class="card card--night card--back-night">
    <div class="services">tembrosk<br>plinsk<br>morvo<br>skandel<br>brunhavel<br>tolpin<br>yusk<br>dwol</div>
    <div class="ghost-name">Quorvix</div>
    <div class="contact">
      <div class="contact__name">John Doe</div>
      <div class="contact__line">123-4567</div>
      <div class="contact__line">Address</div>
      <div class="contact__line">johndoe@email.com</div>
    </div>
  </section>

  <section class="card card--night card--front-night">
    <div class="wordmark">Quorvix</div>
  </section>

  <section class="card card--ice card--back-ice">
    <div class="services">tembrosk<br>plinsk<br>morvo<br>skandel<br>brunhavel<br>tolpin<br>yusk<br>dwol</div>
    <div class="ghost-name">Quorvix</div>
    <div class="contact">
      <div class="contact__name">John Doe</div>
      <div class="contact__line">Phone</div>
      <div class="contact__line">Address</div>
      <div class="contact__line">johndoe@email.com</div>
    </div>
    <div class="edge-strip"></div>
  </section>
</main>
</body>
</html>
```